Webbanner / Banner für Startseite vom Möbel Onlineshop Lunavio18.de
Zielgruppe
Wir sind ein E-Commerce/Onlinehändler im Bereich Home & Living (Schwerpunkt Möbel)
Aufgabenstellung
Es sollen insgesamt drei Bannergrößen erstellt werden (siehe Uploads). Die Banner werden in unserem Shop auf der Startseite eingebunden: www.lunavio18.de
Es sollen Vorlagen sein, dessen Inhalten wir später selbst immer auch ändern können (z. B. das Bewerben von Produkten, einzelnen Kategorien, usw.). Die Texte und das Bildmaterial tauschen wir dann später im Livebetrieb entsprechend selbst aus. Dabei soll das Design/Rahmen der Banner immer gleich sein, sodass wir nur das/die Produktbild(er) und die Texte austauschen.
Die Größen der Banner:
Das Design soll einheitlich sein und zum Shop passen. Wir sind im Bereich Home & Living zuhause, daher sind warme/weiche Designs/Farben von starker Relevanz. Bei Wohnfix9 und Ostbrisejetzt können Sie sich sicherlich Anregungen holen.
Bei Fragen: einfach melden!

```html
<!DOCTYPE html>
<html lang="de">
<head>
<meta charset="utf-8">
<title>Lunavio18.de – Startseiten-Banner</title>
<link rel="stylesheet" href="https://fonts.googleapis.com/css2?family=Raleway:ital,wght@0,400;0,500;0,600;1,500&display=swap">
<style>
  :root {
    --scene-light: #eceae6;
    --scene-mid: #c9c7c3;
    --scene-dark: #8d8b88;
    --scene-warm: #b79a78;
    --paper: #ffffff;
    --band: rgba(255, 255, 255, 0.78);
    --ink: #3c3c3c;
    --button: #4a4a4a;
    --button-text: #ffffff;
  }
  html, body {
    margin: 0;
    padding: 0;
    width: 1200px;
    height: 480px;
    overflow: hidden;
    background: var(--paper);
  }
  .banner {
    position: relative;
    width: 1200px;
    height: 480px;
    overflow: hidden;
    font-family: "Raleway", Arial, sans-serif;
  }
  .banner__photo {
    position: absolute;
    inset: 0;
    background:
      radial-gradient(ellipse at 72% 30%, rgba(183,154,120,0.35), transparent 45%),
      linear-gradient(90deg, var(--scene-light) 0%, var(--scene-mid) 45%, var(--scene-dark) 70%, var(--scene-mid) 100%);
  }
  .banner__brush {
    position: absolute;
    inset: 0;
    width: 1200px;
    height: 480px;
  }
  .banner__frame {
    position: absolute;
    left: 19px;
    top: 19px;
    right: 19px;
    bottom: 19px;
    border: 2px solid var(--paper);
    pointer-events: none;
  }
  .banner__band {
    position: absolute;
    left: 21px;
    right: 21px;
    top: 140px;
    height: 152px;
    background: var(--band);
    display: flex;
    align-items: center;
    justify-content: center;
  }
  .banner__title {
    margin: 0;
    font-size: 64px;
    font-weight: 400;
    color: var(--ink);
    letter-spacing: 0.5px;
  }
  .banner__series {
    font-style: italic;
    font-weight: 500;
  }
  .banner__button {
    position: absolute;
    left: 462px;
    top: 322px;
    width: 346px;
    height: 58px;
    background: var(--button);
    color: var(--button-text);
    display: flex;
    align-items: center;
    justify-content: center;
    font-size: 28px;
    font-weight: 500;
    letter-spacing: 1px;
    text-decoration: none;
  }
</style>
</head>
<body>
  <section class="banner">
    <div class="banner__photo" role="img" aria-label="Wohnzimmer mit weißen Hochglanz-Wohnwandmöbeln, Fernseher und hellem Teppich"></div>

    <svg class="banner__brush" viewBox="0 0 1200 480" aria-hidden="true">
      <path fill="#ffffff" d="M0 0 H170 C120 20 80 60 40 95 C25 110 10 120 0 125 Z"/>
      <path fill="#ffffff" d="M0 340 C40 300 90 285 130 310 C150 330 110 380 90 420 C80 445 85 465 95 480 H0 Z"/>
      <path fill="#ffffff" d="M1200 60 C1150 80 1110 140 1130 180 C1150 215 1120 250 1090 285 C1070 315 1090 350 1130 370 C1160 385 1185 420 1200 440 Z"/>
      <path fill="#ffffff" d="M980 480 C1010 455 1060 440 1100 450 C1130 458 1160 470 1175 480 Z"/>
    </svg>

    <div class="banner__frame"></div>

    <div class="banner__band">
      <h1 class="banner__title"><span class="banner__series">„VELORA“</span> Möbelserie</h1>
    </div>

    <a class="banner__button" href="#">JETZT ANSEHEN</a>
  </section>
</body>
</html>
```